Independent theatre company and venue needs funky web design

Web design for theatre company based in Brisbane Australia. Innovative, grassroots theatre space needs to promote shows in quirky industrial venue. Design needs to be funky, arty but website feels solid and business savvy as well. We need a portal for selling tickets online.
Lamp and Ladder is the production company behind this project. We also create theatre in fresh, intimate and humanistic ways.
Target Market(s)
ages 20s-80s
Interested in the arts and fresh, quirky local experiences
Requirements
Must have
- Pages:
- Performances (What's on)
- Hire the Venue (info and enquiry form)
- About Lamp and Ladder (history and profile)
- Buy Tickets (patrons can purchase tickets to the shows on at the venue)
- Contact Us/Subscribe
Nice to have
- http://www.brickyard27stage.com/
- Similar in content to this one
- Ideally a website I can update shows (so wordpress or similar user friendly)

```html
<!DOCTYPE html>
<html lang="en">
<head>
<meta charset="utf-8">
<title>Lamp and Ladder</title>
<link href="https://fonts.googleapis.com/css2?family=Fira+Sans+Condensed:wght@400;500&family=Roboto:wght@400;500&display=swap" rel="stylesheet">
<style>
:root{
  --page-grey:#e8e8e8;
  --footer-grey:#dcdcdc;
  --white:#ffffff;
  --ink:#2f2f2f;
  --muted:#666666;
  --nav-active:#3c3c3c;
  --panel-dark:#1c1c1c;
  --field:#2c2c2c;
  --field-line:#4a4a4a;
  --accent:#1d9be2;
  --rule:#c9c9c9;
  --icon-grey:#4d4d4d;
}
*{margin:0;padding:0;box-sizing:border-box}
html,body{width:923px;height:1200px;overflow:hidden}
body{position:relative;background:var(--page-grey);font-family:"Roboto",sans-serif;color:var(--ink)}
.abs{position:absolute}
.heading{font-family:"Fira Sans Condensed",sans-serif;font-weight:400;text-transform:uppercase;letter-spacing:.4px}

/* header */
.site-header{left:0;top:0;width:923px;height:138px;background:var(--page-grey)}
.brand{display:flex;align-items:center;gap:7px}
.brand-dot{width:22px;height:22px;border-radius:50%;background:#1a1a1a}
.brand-name{font-family:"Fira Sans Condensed",sans-serif;font-weight:500;font-size:23px;color:#1a1a1a}
.social{left:744px;top:35px;display:flex;gap:5px}
.social span{width:28px;height:28px;border-radius:50%;background:var(--icon-grey);box-shadow:inset 0 0 0 1px rgba(255,255,255,.08)}

.main-nav{left:86px;top:92px;width:751px;height:46px;background:linear-gradient(#3a3a3a,#161616);display:flex}
.main-nav a{color:#fff;text-decoration:none;font-size:9.5px;text-transform:uppercase;display:flex;align-items:center;justify-content:center;height:100%}
.main-nav a.active{background:var(--nav-active)}

/* hero */
.hero-band{left:0;top:138px;width:923px;height:421px;background:var(--white)}
.hero{left:86px;top:138px;width:750px;height:393px;
  background:
    linear-gradient(180deg,rgba(20,4,2,.85) 0%,rgba(20,4,2,0) 10%,rgba(20,4,2,0) 78%,rgba(8,2,1,.9) 100%),
    linear-gradient(90deg,#1a0402 0%,#7a1a06 12%,#e05a0c 30%,#ff9a24 50%,#e05a0c 70%,#6a1204 88%,#0e0201 100%);
  box-shadow:0 14px 14px -10px rgba(0,0,0,.35)}
.hero-caption{left:39px;top:190px;width:335px;height:135px;background:rgba(90,80,30,.72);color:#fff;padding:22px 26px}
.hero-caption h2{font-size:22px;margin-bottom:6px}
.hero-caption p{font-size:9px;line-height:24px;padding-left:2px}
.dots{left:352px;top:370px;display:flex;gap:4px}
.dots span{width:8px;height:8px;background:#222}
.dots span.on{background:#e8e8e8}

/* welcome */
.welcome{left:86px;top:572px;width:751px;height:146px;background:var(--white);box-shadow:0 0 2px rgba(0,0,0,.15)}
.welcome h1{position:absolute;left:25px;top:26px;font-size:22px;color:var(--ink)}
.welcome p{position:absolute;left:28px;top:58px;width:585px;font-size:8.6px;line-height:24px;color:var(--muted)}
.welcome .art{left:628px;top:22px;width:90px;height:104px;border-radius:40% 40% 35% 35%;background:radial-gradient(ellipse at 45% 45%,#f6c8a4 0%,#efb996 60%,#fbeee4 100%)}

/* event cards */
.card{top:736px;width:236px;height:166px;border:2px solid #fff;box-shadow:0 0 2px rgba(0,0,0,.2);overflow:hidden}
.card .photo{left:0;top:0;width:100%;height:100%}
.card .info{left:0;bottom:0;width:100%;height:68px;background:rgba(0,0,0,.55);color:#fff;padding:12px 16px}
.card h3{font-family:"Fira Sans Condensed",sans-serif;font-weight:400;font-size:14px;margin-bottom:3px}
.card p{font-size:8.6px;line-height:16px}

/* subscribe */
.subscribe{left:86px;top:923px;width:751px;height:102px;background:var(--panel-dark)}
.subscribe h2{position:absolute;left:19px;top:19px;font-size:18px;color:#fff}
.field{top:49px;width:197px;height:31px;background:var(--field);border:1px solid var(--field-line);color:#aaa;font-size:8.5px;padding:0 10px;display:flex;align-items:center}
.submit{left:651px;top:49px;width:75px;height:32px;background:var(--accent);color:#fff;font-size:10px;font-weight:500;display:flex;align-items:center;justify-content:center}

/* footer */
.site-footer{left:0;top:1042px;width:923px;height:158px;background:var(--footer-grey)}
.footer-brand{left:86px;top:25px}
.footer-brand .brand-dot{background:#666}
.footer-brand .brand-name{color:#666;font-size:21px}
.legal{left:86px;top:80px;font-size:8px;color:#333}
.copy{left:86px;top:100px;font-size:8.5px;color:#555}
.divider{top:20px;width:1px;height:100px;background:var(--rule)}
.footer-title{top:24px;font-size:12.5px;color:#333}
.links{top:48px;list-style:none;font-size:8.5px;color:#555}
.links li{height:24px}
.map{left:601px;top:50px;width:236px;height:78px;border:2px solid #bbb;background:linear-gradient(120deg,#f4e27a 0%,#ece6c4 22%,#e2e2de 45%,#d6d8dc 70%,#eeeeea 100%)}
.map svg{position:absolute;left:106px;top:14px}
</style>
</head>
<body>

<header class="site-header abs">
  <div class="brand abs" style="left:88px;top:36px">
    <span class="brand-dot"></span><span class="brand-name">Lamp and Ladder</span>
  </div>
  <div class="social abs" aria-label="Social links"><span></span><span></span><span></span></div>
  <nav class="main-nav abs">
    <a class="active" style="width:98px">Home</a>
    <a style="width:118px">Performances</a>
    <a style="width:145px">Hire the Venue</a>
    <a style="width:144px">About Lamp and Ladder</a>
    <a style="width:128px">Buy Tickets</a>
    <a style="width:118px">Contact Us</a>
  </nav>
</header>

<div class="hero-band abs"></div>
<section class="hero abs" role="img" aria-label="Theatre stage with red-orange curtain and audience silhouettes">
  <div class="hero-caption abs">
    <h2 class="heading">Buy Tickets</h2>
    <p>Lorem ipsum dolor sit amet, consectetuer adipiscing elit, sed diam nonummy nibh euismod tincidunt ut laoreet dolore magna aliquam erat volutpat.</p>
  </div>
  <div class="dots abs"><span></span><span></span><span class="on"></span><span></span></div>
</section>

<section class="welcome abs">
  <h1 class="heading">Welcome to Lamp and Ladder</h1>
  <p>Lorem ipsum dolor sit amet, consectetur adipiscing elit. Sed a convallis sapien. Phasellus posuere elementum velit quis interdum. Aliquam ligula tellus, vehicula nec mi nec, iaculis luctus elit. Nullam vel blandit neque. Ut aliquet orci mauris, id fermentum velit fermentum in. Integer id ullamcorper turpis. Ut sit amet nunc ut dui facilisis bibendum ut ut sem. Donec quis risus metus.</p>
  <div class="art abs" role="img" aria-label="Sketched character illustration"></div>
</section>

<article class="card abs" style="left:86px">
  <div class="photo abs" role="img" aria-label="Performers peeking through red stage curtains" style="background:linear-gradient(90deg,#7a0c14 0%,#4a0608 30%,#1a0404 55%,#3a0608 80%,#8a1018 100%)"></div>
  <div class="info abs"><h3>DEC 10, 2015</h3><p>Lorem ipsum dolor sit amet, consectetur adipis cing elit. Sed a convallis sapien.</p></div>
</article>
<article class="card abs" style="left:343px">
  <div class="photo abs" role="img" aria-label="Solo performer under bright stage lights" style="background:radial-gradient(ellipse at 50% 22%,#ffe2c8 0%,#e07a50 22%,#8a2414 50%,#2a0806 85%)"></div>
  <div class="info abs"><h3>DEC 09, 2015</h3><p>Vestibulum venenatis pharetra pellentesque. Praesent condimentum velit elit.</p></div>
</article>
<article class="card abs" style="left:600px">
  <div class="photo abs" role="img" aria-label="Rows of red theatre seats" style="background:linear-gradient(170deg,#2a0806 0%,#8a1c12 30%,#d0402a 55%,#8a1a10 80%,#3a0a06 100%)"></div>
  <div class="info abs"><h3>DEC 08, 2015</h3><p>Morbi aliquet tempus tortor eget aliquet. Curab itur elementum condimentum.</p></div>
</article>

<section class="subscribe abs">
  <h2 class="heading">Subscribe to News</h2>
  <div class="field abs" style="left:19px">First Name</div>
  <div class="field abs" style="left:230px">Last Name</div>
  <div class="field abs" style="left:441px">Email Address</div>
  <div class="submit abs">SUBMIT</div>
</section>

<footer class="site-footer abs">
  <div class="brand footer-brand abs"><span class="brand-dot"></span><span class="brand-name">Lamp and Ladder</span></div>
  <div class="legal abs">Privacy Policy &nbsp;|&nbsp; Sitemap</div>
  <div class="copy abs">Copyrights @ 2015 LampandLadder. All Right Reserved.</div>
  <div class="divider abs" style="left:332px"></div>
  <div class="footer-title heading abs" style="left:363px">Quick Links</div>
  <ul class="links abs" style="left:365px"><li>Performances</li><li>Hire the Venue</li><li>About lamp and ladder</li><li>Buy tickets</li></ul>
  <ul class="links abs" style="left:484px"><li>Privacy Policy</li><li>Sitemap</li><li>Contact Us</li></ul>
  <div class="divider abs" style="left:567px"></div>
  <div class="footer-title heading abs" style="left:601px">Our Location</div>
  <div class="map abs" role="img" aria-label="Street map showing the venue location">
    <svg width="20" height="26" viewBox="0 0 20 26" aria-hidden="true">
      <path d="M10 1C5 1 1.5 4.6 1.5 9.2 1.5 15 10 25 10 25s8.5-10 8.5-15.8C18.5 4.6 15 1 10 1z" fill="#111"/>
      <circle cx="10" cy="9.2" r="3.4" fill="#fff"/>
    </svg>
  </div>
</footer>

</body>
</html>
```